Step-Free Stays Network

We are 100% online, promoting accommodation details and booking facilities for wheelchair dependant travellers.
Listings will only be accommodation providers which meet our specific criteria.

Target Market(s)

Wheelchair dependant people and their companions

Industry/Entity Type

Accommodation

Contact Information for Business Card

Name, mobile phone number, email address, website address

```html
<!DOCTYPE html>
<html lang="en">
<head>
<meta charset="utf-8">
<title>Rollstay Business Card</title>
<link href="https://fonts.googleapis.com/css2?family=Open+Sans:wght@600;700&display=swap" rel="stylesheet">
<style>
  :root {
    --page-bg: #e9e7e4;
    --card-dark: #1d1b1c;
    --card-mid: #2a2728;
    --ink-light: #ffffff;
  }
  html, body {
    margin: 0;
    padding: 0;
    width: 1200px;
    height: 1000px;
    overflow: hidden;
    background: var(--page-bg);
    font-family: "Open Sans", Arial, sans-serif;
  }
  .business-card {
    position: absolute;
    left: 100px;
    top: 214px;
    width: 1000px;
    height: 572px;
    background: radial-gradient(ellipse at 30% 40%, var(--card-mid) 0%, var(--card-dark) 70%);
    color: var(--ink-light);
    box-shadow: 0 8px 30px rgba(0,0,0,0.25);
    overflow: hidden;
  }
  .brand {
    position: absolute;
    left: 80px;
    top: 248px;
    display: flex;
    align-items: center;
    gap: 12px;
  }
  .brand-mark {
    width: 30px;
    height: 30px;
    border: 5px solid var(--ink-light);
    border-radius: 50%;
    box-sizing: border-box;
    flex: none;
  }
  .brand-name {
    font-size: 48px;
    font-weight: 700;
    letter-spacing: -1px;
    line-height: 1;
    white-space: nowrap;
  }
  .brand-tagline {
    position: absolute;
    left: 122px;
    top: 306px;
    font-size: 18px;
    font-weight: 700;
    line-height: 1.15;
  }
  .contact-list {
    position: absolute;
    left: 440px;
    top: 118px;
    margin: 0;
    padding: 0;
    list-style: none;
  }
  .contact-item {
    display: flex;
    align-items: center;
    gap: 18px;
    height: 46px;
    margin-bottom: 18px;
    font-size: 32px;
    font-weight: 700;
    white-space: nowrap;
  }
  .contact-icon {
    width: 36px;
    height: 36px;
    flex: none;
  }
  .holder-name {
    position: absolute;
    left: 410px;
    top: 406px;
    font-size: 34px;
    font-weight: 700;
    letter-spacing: 0.5px;
    white-space: nowrap;
  }
  .holder-rule {
    position: absolute;
    left: 410px;
    top: 456px;
    width: 270px;
    height: 3px;
    background: var(--ink-light);
  }
</style>
</head>
<body>
  <section class="business-card">
    <div class="brand">
      <span class="brand-mark"></span>
      <span class="brand-name">ROLLSTAY</span>
    </div>
    <div class="brand-tagline">Step-Free Stays<br>Network</div>

    <ul class="contact-list">
      <li class="contact-item">
        <svg class="contact-icon" viewBox="0 0 36 36" aria-hidden="true">
          <rect x="8" y="4" width="20" height="28" rx="4" fill="none" stroke="#fff" stroke-width="3"/>
        </svg>
        <span class="contact-text">555-014-2290</span>
      </li>
      <li class="contact-item">
        <svg class="contact-icon" viewBox="0 0 36 36" aria-hidden="true">
          <rect x="3" y="8" width="30" height="20" fill="#fff"/>
          <path d="M3 8 L18 20 L33 8" fill="none" stroke="#1d1b1c" stroke-width="2"/>
        </svg>
        <span class="contact-text">hello@rollstay.com</span>
      </li>
      <li class="contact-item">
        <svg class="contact-icon" viewBox="0 0 36 36" aria-hidden="true">
          <rect x="3" y="6" width="30" height="19" rx="1" fill="none" stroke="#fff" stroke-width="3"/>
          <rect x="13" y="27" width="10" height="4" fill="#fff"/>
        </svg>
        <span class="contact-text">rollstay.com</span>
      </li>
    </ul>

    <div class="holder-name">DANA RUELLE</div>
    <div class="holder-rule"></div>
  </section>
</body>
</html>
```